Book Cover " FROM GRAVEL TO AMBER"

Looking for a book cover for a novel from Gravel to Amber.
Amber is the characters developed name. The book describes his rough up bringing and how he obtains his greatness and his given name Amber.

```html
<!DOCTYPE html>
<html lang="en">
<head>
<meta charset="UTF-8">
<title>From Gravel to Amber — Book Cover</title>
<link rel="stylesheet" href="https://fonts.googleapis.com/css2?family=Permanent+Marker&family=Montserrat:wght@700&family=Libre+Baskerville&display=swap">
<style>
  :root {
    --paper: #ffffff;
    --ink: #111111;
    --wash-light: #4f95e6;
    --wash-mid: #2c72d6;
    --wash-deep: #1b5cc7;
    --title-light: #ffffff;
  }
  html, body {
    margin: 0;
    padding: 0;
    width: 800px;
    height: 1200px;
    overflow: hidden;
    background: var(--paper);
  }
  .cover {
    position: relative;
    width: 800px;
    height: 1200px;
    background: var(--paper);
    overflow: hidden;
  }
  .cover__wash {
    position: absolute;
    left: 0;
    top: 0;
    width: 800px;
    height: 1200px;
    display: block;
  }
  .cover__title-top {
    position: absolute;
    left: 0;
    right: 0;
    top: 318px;
    margin: 0;
    text-align: center;
    font-family: "Permanent Marker", cursive;
    font-weight: 400;
    font-size: 66px;
    letter-spacing: 1px;
    color: var(--ink);
    transform: skewX(-6deg);
  }
  .cover__title-bottom {
    position: absolute;
    left: 0;
    right: 0;
    top: 670px;
    margin: 0;
    text-align: center;
    font-family: "Montserrat", sans-serif;
    font-weight: 700;
    font-size: 82px;
    letter-spacing: 14px;
    color: var(--title-light);
  }
  .cover__author {
    position: absolute;
    left: 0;
    right: 0;
    top: 1064px;
    margin: 0;
    text-align: center;
    font-family: "Libre Baskerville", serif;
    font-size: 40px;
    letter-spacing: 9px;
    color: var(--title-light);
  }
</style>
</head>
<body>
  <main class="cover">
    <svg class="cover__wash" viewBox="0 0 800 1200" role="img" aria-label="Blue watercolour wash filling the lower part of the cover with a soft, uneven top edge">
      <defs>
        <linearGradient id="washGradient" x1="0" y1="0" x2="0.3" y2="1">
          <stop offset="0" stop-color="var(--wash-light)"/>
          <stop offset="0.45" stop-color="var(--wash-mid)"/>
          <stop offset="1" stop-color="var(--wash-deep)"/>
        </linearGradient>
      </defs>
      <path fill="url(#washGradient)"
        d="M0 470 C40 458 70 472 110 462 C150 452 180 468 220 456 C260 446 300 462 340 452
           C380 444 420 458 460 448 C500 440 540 456 580 446 C620 438 660 452 700 442
           C740 436 770 448 800 440 L800 1200 L0 1200 Z"/>
    </svg>
    <h1 class="cover__title-top">FROM GRAVEL</h1>
    <p class="cover__title-bottom">TO AMBER</p>
    <p class="cover__author">AUTHOR NAME</p>
  </main>
</body>
</html>
```